Flyer design for retail store owners

i would need to have a flyer design for my retail shop customers to show that I am a mailbox store that has all major shipping vendors to for their shipping needs. Ensuring that they can take advantage of opening a house account at the store and billed monthly, word document has all the details. Please use stock images for the notary public, passport photos, mailbox brass pictures of my actual mailboxes are listed in the pictures. I need to make it POP and WOW these retail store owners as I am using it to advertise the business

```html
<!DOCTYPE html>
<html lang="en">
<head>
<meta charset="utf-8">
<title>Mailbox Rental Flyer</title>
<link href="https://fonts.googleapis.com/css2?family=Fira+Sans+Extra+Condensed:wght@600;700&family=Lato:ital,wght@0,400;0,700;1,400;1,700&display=swap" rel="stylesheet">
<style>
  :root{
    --stage:#e49b82;
    --paper:#f1f1f3;
    --paper-shade:#e3e3e8;
    --orange-top:#f5a52a;
    --orange-bottom:#e5622a;
    --navy:#2e2a78;
    --white:#ffffff;
    --gold-light:#d9b877;
    --gold-dark:#8a6a2c;
  }
  *{box-sizing:border-box;margin:0;padding:0}
  html,body{width:1200px;height:959px;overflow:hidden;background:var(--stage)}
  .stage{position:relative;width:1200px;height:959px}
  .page{position:absolute;top:117px;width:560px;height:725px;background:var(--paper);overflow:hidden;
        box-shadow:0 18px 40px rgba(120,50,30,.25)}
  .page--front{left:27px}
  .page--back{left:613px}
  .page-art{position:absolute;inset:0;width:560px;height:725px}
  .headline{position:absolute;left:38px;top:196px;font-family:"Fira Sans Extra Condensed",sans-serif;font-weight:700;
            font-size:70px;line-height:.95;color:var(--white);text-shadow:3px 4px 4px rgba(90,40,10,.45)}
  .intro{position:absolute;left:40px;top:350px;width:330px;font-family:"Lato",sans-serif;font-weight:700;
         font-size:11.6px;line-height:1.4;color:var(--white)}
  .promo-badge{position:absolute;left:402px;top:360px;width:140px;height:140px;border-radius:50%;
               background:var(--orange-top);border:9px solid var(--navy);color:var(--white);
               font-family:"Lato",sans-serif;text-align:center;padding-top:16px}
  .promo-badge .kicker{font-size:11px;font-weight:700;line-height:1.1}
  .promo-badge .price{font-family:"Fira Sans Extra Condensed",sans-serif;font-size:50px;font-weight:700;line-height:1}
  .promo-badge .terms{font-size:9.5px;font-weight:700;line-height:1.1}
  .limited{position:absolute;right:0;top:524px;width:250px;height:30px;padding-left:46px;
           font-family:"Lato",sans-serif;font-style:italic;font-size:12px;color:var(--white);line-height:30px}
  .about{position:absolute;left:40px;top:612px;width:490px;font-family:"Lato",sans-serif;font-weight:700;
         font-size:11.2px;line-height:1.42;color:var(--navy)}
  .back-copy{position:absolute;left:40px;top:256px;width:280px;font-family:"Lato",sans-serif;font-style:italic;
             font-size:10.5px;line-height:1.42;color:var(--white)}
  .deals-title{position:absolute;left:40px;top:384px;font-family:"Lato",sans-serif;font-style:italic;font-weight:700;
               font-size:13px;color:var(--white)}
  .deals{position:absolute;left:34px;top:406px;width:320px;list-style:none;font-family:"Lato",sans-serif;
         font-style:italic;font-size:10.2px;line-height:1.35;color:var(--white)}
  .deals li{position:relative;padding-left:18px;margin-bottom:3px}
  .deals svg{position:absolute;left:0;top:2px;width:11px;height:11px}
</style>
</head>
<body>
<div class="stage">

  <section class="page page--front">
    <svg class="page-art" viewBox="0 0 560 725">
      <defs>
        <linearGradient id="orangeFront" x1="0" y1="0" x2="0" y2="1">
          <stop offset="0" stop-color="var(--orange-top)"/>
          <stop offset="1" stop-color="var(--orange-bottom)"/>
        </linearGradient>
        <linearGradient id="goldPhoto" x1="0" y1="0" x2="1" y2="1">
          <stop offset="0" stop-color="var(--gold-light)"/>
          <stop offset="1" stop-color="var(--gold-dark)"/>
        </linearGradient>
        <linearGradient id="fadePhoto" x1="0" y1="0" x2="0" y2="1">
          <stop offset="0" stop-color="#d8d3c8"/>
          <stop offset="1" stop-color="#f2f1ef"/>
        </linearGradient>
      </defs>
      <polygon points="0,40 120,0 560,0 560,160" fill="var(--paper-shade)"/>
      <polygon points="0,225 205,20 270,20 505,255 420,345 560,485 560,555 0,555" fill="url(#orangeFront)"/>
      <polygon points="0,215 70,145 95,145 0,240" fill="var(--navy)"/>
      <polygon points="0,60 35,40 0,90" fill="var(--navy)"/>
      <polygon points="300,555 340,518 560,518 560,555" fill="var(--navy)"/>
      <polygon points="420,500 470,470 470,500" fill="var(--navy)"/>
      <rect x="0" y="555" width="560" height="170" fill="url(#fadePhoto)" role="img" aria-label="Faded photo of a wall of brass mailboxes"/>
      <polygon points="158,140 280,210 190,165" fill="var(--navy)"/>
      <rect x="268" y="22" width="250" height="228" fill="url(#goldPhoto)" role="img" aria-label="Photo of a brass mailbox cabinet with locking doors"/>
      <circle cx="112" cy="105" r="78" fill="url(#goldPhoto)" stroke="var(--navy)" stroke-width="7" role="img" aria-label="Close-up photo of an open mailbox door"/>
    </svg>
    <h1 class="headline">Renting<br>a mail box</h1>
    <p class="intro">Renting a mail box is one of the most efficient and cost saving methods for receiving your mail and packages. Instead of having to worry about private security, weather conditions, sorting, and deliveries; all you have to do is pick-up your mail from our secured facility each day except Sundays. You will get a notification when mail arrives whether envelope or package, it will be scanned in daily which other mailbox stores do not offer! We offer onsite Notary Public with no appointments and onsite Passport Photos and can ship out same day.</p>
    <div class="promo-badge">
      <div class="kicker">exclusive<br>promo deal!</div>
      <div class="price">$12</div>
      <div class="terms">a month for 6-12<br>months leases!</div>
    </div>
    <div class="limited">Take advantage of this limited time offer!</div>
    <p class="about">At Swift Parcel Hub, our goal is to make your shipping experience as convenient as possible. Whether you are shipping packages, documents, or packages, we are here to help. Whether you want to package or estimate the price of your package, it is easy for you. We are ready to handle all services! Get also the services you need; printing, copying, and stop in to purchase postal materials. Service point partners are Northline Freight, ParcelAir, Civic Post, and GlobeXpress.</p>
  </section>

  <section class="page page--back">
    <svg class="page-art" viewBox="0 0 560 725">
      <defs>
        <linearGradient id="orangeBack" x1="0" y1="0" x2="0" y2="1">
          <stop offset="0" stop-color="var(--orange-top)"/>
          <stop offset="1" stop-color="var(--orange-bottom)"/>
        </linearGradient>
        <linearGradient id="sealPhoto" x1="0" y1="0" x2="1" y2="1">
          <stop offset="0" stop-color="#5a4a40"/>
          <stop offset="1" stop-color="#d8d0c6"/>
        </linearGradient>
        <linearGradient id="blurPhoto" x1="0" y1="0" x2="1" y2="1">
          <stop offset="0" stop-color="#b8913e"/>
          <stop offset="1" stop-color="#7a5e28"/>
        </linearGradient>
        <radialGradient id="passPhoto">
          <stop offset="0" stop-color="#f4f4f6"/>
          <stop offset="1" stop-color="#c9cbd6"/>
        </radialGradient>
      </defs>
      <polygon points="0,0 560,0 560,40 0,90" fill="var(--paper-shade)"/>
      <polygon points="0,145 135,10 260,10 560,310 560,460 470,555 0,555" fill="url(#orangeBack)"/>
      <polygon points="0,120 40,80 75,80 0,155" fill="var(--navy)"/>
      <polygon points="370,555 450,475 500,460 500,500 445,555" fill="var(--navy)"/>
      <polygon points="470,555 560,465 560,555" fill="var(--paper-shade)"/>
      <g transform="rotate(45 490 220)">
        <rect x="370" y="100" width="240" height="240" rx="20" fill="url(#sealPhoto)" stroke="var(--white)" stroke-width="6" role="img" aria-label="Photo of a wax seal stamp on a rolled document"/>
      </g>
      <circle cx="150" cy="115" r="88" fill="url(#passPhoto)" stroke="var(--navy)" stroke-width="8" role="img" aria-label="Illustration of two passports with boarding passes"/>
      <rect x="0" y="555" width="560" height="170" fill="url(#blurPhoto)" role="img" aria-label="Blurred photo of numbered brass mailboxes"/>
    </svg>
    <p class="back-copy">Now renting mailboxes on Maple Ridge Plaza. We are offering all Maple Ridge Plaza owners/employees an exclusive promo deal! $12 a month for 6-12 months leases! You get a mailbox in the shop, a book of stamps(20 count), 3 notarizations by appointment, 100 copies of black and white, and 100 copies of color. Please see associate for sign up!</p>
    <h2 class="deals-title">CHECK OUT THESE OTHER DEALS!</h2>
    <ul class="deals">
      <li><svg viewBox="0 0 12 12"><circle cx="6" cy="6" r="5" fill="none" stroke="currentColor"/><path d="M3.5 6l2 2 4-4.5" fill="none" stroke="currentColor" stroke-width="1.4"/></svg>As a retail owner, you know how important it is to keep your customers coming back - you will get 20% discount for printing services.</li>
      <li><svg viewBox="0 0 12 12"><circle cx="6" cy="6" r="5" fill="none" stroke="currentColor"/><path d="M3.5 6l2 2 4-4.5" fill="none" stroke="currentColor" stroke-width="1.4"/></svg>We duplicate keys for $2/each, our regular price charge is $4/each. Save up to 50%!</li>
      <li><svg viewBox="0 0 12 12"><circle cx="6" cy="6" r="5" fill="none" stroke="currentColor"/><path d="M3.5 6l2 2 4-4.5" fill="none" stroke="currentColor" stroke-width="1.4"/></svg>Lamination is also discounted at 10% off.</li>
      <li><svg viewBox="0 0 12 12"><circle cx="6" cy="6" r="5" fill="none" stroke="currentColor"/><path d="M3.5 6l2 2 4-4.5" fill="none" stroke="currentColor" stroke-width="1.4"/></svg>10% off retail supplies ... must be minimum of 10$</li>
      <li><svg viewBox="0 0 12 12"><circle cx="6" cy="6" r="5" fill="none" stroke="currentColor"/><path d="M3.5 6l2 2 4-4.5" fill="none" stroke="currentColor" stroke-width="1.4"/></svg>For house accounts -a 5% discount will be deducted monthly of billing change to invoicing PLUS we're giving another 5% of the discount if you upgrade and sign up for mailbox. Great right?</li>
    </ul>
  </section>

</div>
</body>
</html>
```